Quilvo Garage Doors Business Card

I need a Business Card for my garage door business:
Quilvo Garage Doors.
please add:
logo
phone number: 855-3-QUILVO
(853-392)

email: service@quilvogaragedoors.com
website: www.quilvogaragedoors.com

The attached image is recommendation ONLY.

```html
<!DOCTYPE html>
<html lang="en">
<head>
<meta charset="utf-8">
<title>Quilvo Garage Doors Business Card</title>
<link href="https://fonts.googleapis.com/css2?family=Josefin+Sans:wght@300;400;600&display=swap" rel="stylesheet">
<style>
  :root {
    --page-bg: #d9d6d1;
    --card-bg: #eceeef;
    --card-edge: #ffffff;
    --brand-teal: #2a9a9d;
    --ink-dark: #1d2326;
    --ink-light: #f2fbfb;
  }
  html, body {
    margin: 0;
    padding: 0;
    width: 1200px;
    height: 969px;
    overflow: hidden;
    background: var(--page-bg);
    font-family: "Josefin Sans", sans-serif;
  }
  .business-card {
    position: absolute;
    left: 100px;
    top: 199px;
    width: 1000px;
    height: 571px;
    background: var(--card-bg);
    border: 2px solid var(--card-edge);
    border-radius: 22px;
    overflow: hidden;
    box-sizing: border-box;
  }
  .brand-mark {
    position: absolute;
    left: 55px;
    top: 50px;
    display: flex;
    align-items: center;
    gap: 26px;
  }
  .brand-dot {
    width: 110px;
    height: 110px;
    border-radius: 50%;
    background: var(--brand-teal);
  }
  .brand-name {
    margin: 0;
    font-weight: 600;
    font-size: 44px;
    line-height: 1.05;
    color: var(--ink-dark);
  }
  .contact-panel {
    position: absolute;
    left: 494px;
    top: 103px;
    width: 506px;
    height: 468px;
  }
  .contact-panel svg.panel-shape {
    position: absolute;
    inset: 0;
  }
  .contact-details {
    position: absolute;
    right: 54px;
    top: 0;
    text-align: right;
    color: var(--ink-light);
  }
  .person-name {
    position: absolute;
    right: 0;
    top: 160px;
    margin: 0;
    font-weight: 600;
    font-size: 34px;
    white-space: nowrap;
  }
  .person-title {
    position: absolute;
    right: 0;
    top: 205px;
    margin: 0;
    font-weight: 400;
    font-size: 25px;
    white-space: nowrap;
  }
  .contact-list {
    position: absolute;
    right: 0;
    top: 262px;
    margin: 0;
    padding: 0;
    list-style: none;
  }
  .contact-item {
    display: flex;
    justify-content: flex-end;
    align-items: center;
    gap: 12px;
    height: 40px;
    font-weight: 300;
    font-size: 25px;
    white-space: nowrap;
  }
  .contact-item svg {
    width: 22px;
    height: 22px;
    flex: none;
  }
</style>
</head>
<body>
  <div class="business-card">
    <div class="brand-mark">
      <div class="brand-dot"></div>
      <p class="brand-name">Quilvo<br>Garage Doors</p>
    </div>

    <div class="contact-panel">
      <svg class="panel-shape" width="506" height="468" viewBox="0 0 506 468">
        <path d="M0 468 L0 130 Q0 112 16 104 L238 6 Q254 0 270 6 L506 104 L506 468 Z" fill="var(--brand-teal)"/>
      </svg>
      <div class="contact-details">
        <p class="person-name">Daniel Reyes</p>
        <p class="person-title">CEO/Founder</p>
        <ul class="contact-list">
          <li class="contact-item">855-3-QUILVO
            <svg viewBox="0 0 24 24"><path fill="#f2fbfb" d="M6.6 10.8a15.1 15.1 0 0 0 6.6 6.6l2.2-2.2a1 1 0 0 1 1-.25 11.4 11.4 0 0 0 3.6.57 1 1 0 0 1 1 1V20a1 1 0 0 1-1 1A17 17 0 0 1 3 4a1 1 0 0 1 1-1h3.5a1 1 0 0 1 1 1c0 1.25.2 2.45.57 3.6a1 1 0 0 1-.25 1z"/></svg>
          </li>
          <li class="contact-item">(853-392)
            <svg viewBox="0 0 24 24"><path fill="#f2fbfb" d="M6.6 10.8a15.1 15.1 0 0 0 6.6 6.6l2.2-2.2a1 1 0 0 1 1-.25 11.4 11.4 0 0 0 3.6.57 1 1 0 0 1 1 1V20a1 1 0 0 1-1 1A17 17 0 0 1 3 4a1 1 0 0 1 1-1h3.5a1 1 0 0 1 1 1c0 1.25.2 2.45.57 3.6a1 1 0 0 1-.25 1z"/></svg>
          </li>
          <li class="contact-item">service@quilvogaragedoors.com
            <svg viewBox="0 0 24 24"><rect x="2" y="5" width="20" height="14" rx="1.5" fill="#f2fbfb"/><path d="M3 6.5 12 13l9-6.5" fill="none" stroke="#2a9a9d" stroke-width="1.6"/></svg>
          </li>
          <li class="contact-item">www.quilvogaragedoors.com
            <svg viewBox="0 0 24 24"><circle cx="12" cy="12" r="10" fill="#f2fbfb"/><path d="M12 2v20M2 12h20M12 2c-4 4-4 16 0 20M12 2c4 4 4 16 0 20" fill="none" stroke="#2a9a9d" stroke-width="1.3"/></svg>
          </li>
        </ul>
      </div>
    </div>
  </div>
</body>
</html>
```